Banner Ad Design Project

Process description of accounting delivery A to Z

Your folder appointment for delivery of receipts, in and outgoing invoices not necessary but possible – goes into a industrial sized scanner at the office

Electronic delivery via email, CloudDrop or remote scanning locally at the clients office

Imported into the accounting software (called Ledgerly) with drag and drop from email and CloudDrop our directly imported from scanner at clients office

Software sets ledger accounts after scanning largely automated
Imported into accounting softer and finished by producing Income statement , Balance sheet and cash flow statements.

Size should fit the www.fennivar.no webpage banners rolling

Target Market(s)

New Clients - its to sell our work as modern

Industry/Entity Type

Accounting

Requirements
Must have
• Color scheme fitting current webpage. Looking for a process driven illustration where details are more 1D not 3D as such. Simplified and easy to grasp scheme of flow in our production pipeline.

```html
<!DOCTYPE html>
<html lang="en">
<head>
<meta charset="utf-8">
<title>fennivar – Delivery Process Banners</title>
<link href="https://fonts.googleapis.com/css2?family=Hind:wght@400;500;600&display=swap" rel="stylesheet">
<style>
  :root {
    --page-bg: #efefef;
    --banner-bg: #ffffff;
    --brand-green: #1f8a6b;
    --ink: #3a3a3a;
    --ink-soft: #555555;
    --rule: #b8b8b8;
    --step-ring: #8a8a8a;
  }
  * { box-sizing: border-box; margin: 0; padding: 0; }
  html, body { width: 1200px; height: 1000px; overflow: hidden; background: var(--page-bg); }
  body { position: relative; font-family: "Hind", "Helvetica Neue", Arial, sans-serif; color: var(--ink); }

  .banner { position: absolute; left: 216px; width: 768px; height: 240px; background: var(--banner-bg); }
  .banner--en { top: 200px; }
  .banner--no { top: 537px; }
  .banner > * { position: absolute; }

  .brand { left: 33px; top: 0; width: 96px; height: 54px; display: flex; align-items: center; justify-content: center; }
  .brand__name { font-size: 22px; font-weight: 500; color: var(--brand-green); letter-spacing: 0.2px; }

  .banner__title { top: 18px; left: 0; width: 768px; padding-left: 16px; text-align: center; font-size: 17px; font-weight: 600; letter-spacing: 0.3px; }

  .step-num { width: 18px; height: 18px; border: 2px solid var(--step-ring); border-radius: 50%; font-size: 11px; font-weight: 600; color: var(--step-ring); display: flex; align-items: center; justify-content: center; line-height: 1; padding-top: 2px; }
  .step-title { font-size: 14px; font-weight: 500; line-height: 1; white-space: nowrap; }
  .option { font-size: 12.5px; font-weight: 500; line-height: 1; white-space: nowrap; }
  .note { font-size: 10px; color: var(--ink-soft); line-height: 11px; white-space: nowrap; }
  .connector { font-size: 13px; line-height: 1; }

  .product-badge { left: 358px; top: 104px; width: 94px; height: 26px; background: var(--brand-green); color: #fff; font-size: 17px; font-weight: 600; display: flex; align-items: center; justify-content: center; padding-top: 3px; }

  .divider { top: 70px; width: 0; height: 146px; border-left: 1.5px dashed var(--rule); }
  .divider--1 { left: 278px; }
  .divider--2 { left: 520px; }

  .phase { top: 224px; height: 12px; display: flex; align-items: center; gap: 8px; font-size: 10px; color: var(--ink-soft); }
  .phase::before, .phase::after { content: ""; flex: 1; border-top: 1.5px dashed var(--rule); }
  .phase--1 { left: 32px; width: 232px; }
  .phase--2 { left: 292px; width: 214px; }
  .phase--3 { left: 535px; width: 202px; }

  .flow-arrow { top: 217px; width: 18px; height: 18px; }
  .cloud-name { font-size: 18px; color: var(--ink); letter-spacing: -0.2px; line-height: 1; }
  .icon { display: block; }
</style>
</head>
<body>

<svg width="0" height="0" style="position:absolute">
  <defs>
    <symbol id="ico-voucher" viewBox="0 0 28 30">
      <rect x="1.5" y="1.5" width="25" height="27" fill="none" stroke="#1f8a6b" stroke-width="2" stroke-dasharray="2 1.4"/>
      <rect x="6" y="6" width="5" height="4" fill="#1f8a6b"/>
      <rect x="6" y="12" width="10" height="1.6" fill="#1f8a6b"/>
      <rect x="6" y="15.5" width="8" height="1.6" fill="#1f8a6b"/>
      <text x="19" y="24" font-size="8" font-weight="700" fill="#1f8a6b" font-family="Arial, sans-serif">$</text>
    </symbol>
    <symbol id="ico-scanner" viewBox="0 0 36 34">
      <path d="M4 20 L20 2 L28 6 L13 23 Z" fill="none" stroke="#3a3a3a" stroke-width="2.4"/>
      <path d="M2 22 L34 22 L34 30 L2 30 Z" fill="#3a3a3a"/>
      <rect x="6" y="25" width="22" height="1.5" fill="#fff"/>
    </symbol>
    <symbol id="ico-mail" viewBox="0 0 30 22">
      <rect x="1.5" y="1.5" width="27" height="19" rx="2" fill="none" stroke="#1f8a6b" stroke-width="2.4"/>
      <path d="M2 3 L15 13 L28 3" fill="none" stroke="#1f8a6b" stroke-width="2.4"/>
    </symbol>
    <symbol id="ico-monitor" viewBox="0 0 32 26">
      <rect x="1.5" y="1.5" width="29" height="17" fill="none" stroke="#1f8a6b" stroke-width="2.4"/>
      <rect x="10" y="21" width="12" height="3" fill="#1f8a6b"/>
      <path d="M10 9 A8 8 0 0 1 22 9 M12.5 11.5 A4.5 4.5 0 0 1 19.5 11.5" fill="none" stroke="#3a3a3a" stroke-width="1.6"/>
      <circle cx="16" cy="14" r="1.3" fill="#3a3a3a"/>
    </symbol>
    <symbol id="ico-phone" viewBox="0 0 12 28">
      <rect x="0.5" y="0.5" width="11" height="27" rx="1.5" fill="#1f8a6b"/>
      <rect x="2" y="3" width="8" height="20" fill="#3a3a3a" opacity="0.35"/>
    </symbol>
    <symbol id="ico-stack" viewBox="0 0 32 36">
      <rect x="1" y="1" width="24" height="30" fill="#fff" stroke="#3a3a3a" stroke-width="1.6"/>
      <rect x="3" y="2.5" width="24" height="30" fill="#fff" stroke="#3a3a3a" stroke-width="1.6"/>
      <rect x="5" y="4" width="24" height="30" fill="#fff" stroke="#3a3a3a" stroke-width="1.6"/>
      <rect x="9" y="9" width="7" height="5" fill="#3a3a3a"/>
      <rect x="9" y="17" width="16" height="1.6" fill="#3a3a3a"/>
      <rect x="9" y="21" width="16" height="1.6" fill="#3a3a3a"/>
      <rect x="9" y="25" width="12" height="1.6" fill="#3a3a3a"/>
    </symbol>
    <symbol id="ico-chevrons" viewBox="0 0 16 14">
      <path d="M1 1 L7 7 L1 13 H5 L11 7 L5 1 Z M6 1 L12 7 L6 13 H10 L16 7 L10 1 Z" fill="#1f8a6b"/>
    </symbol>
    <symbol id="ico-ledger" viewBox="0 0 30 36">
      <path d="M1.5 1.5 H20 L28.5 10 V34.5 H1.5 Z" fill="#fff" stroke="#1f8a6b" stroke-width="2.2"/>
      <path d="M20 1.5 V10 H28.5" fill="none" stroke="#1f8a6b" stroke-width="2"/>
      <rect x="6" y="8" width="10" height="1.6" fill="#1f8a6b"/>
      <rect x="6" y="12" width="14" height="1.6" fill="#1f8a6b"/>
      <rect x="6" y="16" width="8" height="1.6" fill="#1f8a6b"/>
      <circle cx="21" cy="27" r="5" fill="none" stroke="#1f8a6b" stroke-width="1.6"/>
      <circle cx="21" cy="27" r="2" fill="#1f8a6b"/>
    </symbol>
    <symbol id="ico-report-text" viewBox="0 0 26 36">
      <path d="M1 1 H17 L25 9 V35 H1 Z" fill="#fff" stroke="#3a3a3a" stroke-width="1.8"/>
      <path d="M17 1 V9 H25" fill="none" stroke="#3a3a3a" stroke-width="1.6"/>
      <g fill="#3a3a3a"><rect x="5" y="12" width="4" height="1.5"/><rect x="11" y="12" width="9" height="1.5"/><rect x="5" y="16" width="4" height="1.5"/><rect x="11" y="16" width="9" height="1.5"/><rect x="5" y="20" width="4" height="1.5"/><rect x="11" y="20" width="9" height="1.5"/><rect x="5" y="24" width="4" height="1.5"/><rect x="11" y="24" width="9" height="1.5"/><rect x="5" y="28" width="4" height="1.5"/><rect x="11" y="28" width="7" height="1.5"/></g>
    </symbol>
    <symbol id="ico-report-sheet" viewBox="0 0 28 36">
      <rect x="1" y="1" width="26" height="34" fill="#fff" stroke="#1f8a6b" stroke-width="1.8"/>
      <rect x="5" y="5" width="7" height="6" fill="none" stroke="#1f8a6b" stroke-width="1.4"/>
      <g fill="#1f8a6b"><rect x="14" y="6" width="9" height="1.5"/><rect x="14" y="9" width="9" height="1.5"/><rect x="5" y="14" width="18" height="1.5"/><rect x="5" y="18" width="18" height="1.5"/><rect x="5" y="22" width="18" height="1.5"/><rect x="5" y="26" width="18" height="1.5"/><rect x="5" y="30" width="18" height="1.5"/></g>
    </symbol>
    <symbol id="ico-report-cash" viewBox="0 0 28 36">
      <path d="M1 1 H20 L27 8 V35 H1 Z" fill="#fff" stroke="#3a3a3a" stroke-width="1.8"/>
      <text x="15" y="14" font-size="10" font-weight="700" fill="#3a3a3a" font-family="Arial, sans-serif">$</text>
      <g fill="#3a3a3a"><rect x="5" y="6" width="7" height="1.5"/><rect x="5" y="10" width="7" height="1.5"/><rect x="5" y="18" width="18" height="1.8"/><rect x="5" y="22" width="18" height="1.8"/><rect x="5" y="26" width="18" height="1.8"/><rect x="5" y="30" width="18" height="1.8"/></g>
    </symbol>
    <symbol id="ico-flow" viewBox="0 0 18 18">
      <circle cx="9" cy="9" r="7.6" fill="#fff" stroke="#9a9a9a" stroke-width="1.6"/>
      <path d="M5 9 H12.5 M9.5 5.8 L12.8 9 L9.5 12.2" fill="none" stroke="#9a9a9a" stroke-width="1.6"/>
    </symbol>
  </defs>
</svg>

<!-- English banner -->
<section class="banner banner--en">
  <div class="brand"><span class="brand__name">fennivar</span></div>
  <h1 class="banner__title">Standard &amp; Digital Delivery Process</h1>

  <div class="step-num" style="left:27px;top:69px">1</div>
  <p class="step-title" style="left:50px;top:74px">Client delivers vouchers either</p>
  <p class="option" style="left:50px;top:98px">a. manually for scanning</p>
  <p class="note" style="left:63px;top:109px">and we prepare them<br>for ledger entry</p>
  <p class="connector" style="left:51px;top:137px">or</p>
  <p class="option" style="left:50px;top:160px">b. electronically</p>
  <p class="note" style="left:63px;top:172px">via email, CloudDrop or remote scanning</p>

  <svg class="icon" style="left:188px;top:118px" width="27" height="29"><use href="#ico-voucher"/></svg>
  <span style="left:219px;top:120px;font-size:16px;font-weight:600">+</span>
  <svg class="icon" style="left:226px;top:114px" width="34" height="32"><use href="#ico-scanner"/></svg>

  <svg class="icon" style="left:68px;top:190px" width="30" height="22"><use href="#ico-mail"/></svg>
  <span class="cloud-name" style="left:106px;top:195px">CloudDrop</span>
  <svg class="icon" style="left:205px;top:186px" width="32" height="26"><use href="#ico-monitor"/></svg>
  <svg class="icon" style="left:239px;top:186px" width="11" height="27"><use href="#ico-phone"/></svg>

  <div class="divider divider--1"></div>
  <div class="divider divider--2"></div>

  <div class="step-num" style="left:292px;top:69px">2</div>
  <p class="step-title" style="left:315px;top:74px">Import to accounting software</p>
  <p class="note" style="left:315px;top:87px">directly from scanner or by drag and drop</p>
  <div class="product-badge">Ledgerly</div>

  <div class="step-num" style="left:292px;top:146px">3</div>
  <p class="step-title" style="left:315px;top:151px">The software creates ledger</p>
  <p class="note" style="left:315px;top:163px">for each account</p>
  <svg class="icon" style="left:357px;top:178px" width="32" height="36"><use href="#ico-stack"/></svg>
  <svg class="icon" style="left:398px;top:192px" width="15" height="13"><use href="#ico-chevrons"/></svg>
  <svg class="icon" style="left:423px;top:178px" width="30" height="36"><use href="#ico-ledger"/></svg>

  <div class="step-num" style="left:537px;top:69px">4</div>
  <p class="step-title" style="left:561px;top:74px">Generate reports</p>
  <p class="note" style="left:561px;top:87px">Income statement, balance sheet and<br>Cash flow statement</p>
  <svg class="icon" style="left:618px;top:116px" width="25" height="36"><use href="#ico-report-text"/></svg>
  <svg class="icon" style="left:655px;top:116px" width="28" height="36"><use href="#ico-report-sheet"/></svg>
  <svg class="icon" style="left:696px;top:116px" width="28" height="36"><use href="#ico-report-cash"/></svg>

  <div class="phase phase--1">Delivery</div>
  <div class="phase phase--2">Processing</div>
  <div class="phase phase--3">Finalisation</div>
  <svg class="flow-arrow" style="left:269px"><use href="#ico-flow"/></svg>
  <svg class="flow-arrow" style="left:511px"><use href="#ico-flow"/></svg>
</section>

<!-- Norwegian banner -->
<section class="banner banner--no" lang="no">
  <div class="brand"><span class="brand__name">fennivar</span></div>
  <h1 class="banner__title" style="padding-left:0;padding-right:24px">Standard &amp; Elektronisk - leveringsprosess</h1>

  <div class="step-num" style="left:27px;top:69px">1</div>
  <p class="step-title" style="left:50px;top:74px">Kunden leverer enten</p>
  <p class="option" style="left:50px;top:98px">a. manuelt bilag til skanning</p>
  <p class="note" style="left:63px;top:109px">og vi klargjør for føring</p>
  <p class="connector" style="left:51px;top:137px">eller</p>
  <p class="option" style="left:50px;top:160px">b. elektronisk</p>
  <p class="note" style="left:63px;top:172px">via email, CloudDrop eller fjernskanning</p>

  <svg class="icon" style="left:188px;top:118px" width="27" height="29"><use href="#ico-voucher"/></svg>
  <span style="left:219px;top:120px;font-size:16px;font-weight:600">+</span>
  <svg class="icon" style="left:226px;top:114px" width="34" height="32"><use href="#ico-scanner"/></svg>

  <svg class="icon" style="left:68px;top:190px" width="30" height="22"><use href="#ico-mail"/></svg>
  <span class="cloud-name" style="left:106px;top:195px">CloudDrop</span>
  <svg class="icon" style="left:205px;top:186px" width="32" height="26"><use href="#ico-monitor"/></svg>
  <svg class="icon" style="left:239px;top:186px" width="11" height="27"><use href="#ico-phone"/></svg>

  <div class="divider divider--1"></div>
  <div class="divider divider--2"></div>

  <div class="step-num" style="left:292px;top:69px">2</div>
  <p class="step-title" style="left:315px;top:74px">Importeres til Ledgerly</p>
  <p class="note" style="left:315px;top:87px">direkte fra skanner eller via dra og slipp</p>
  <div class="product-badge">Ledgerly</div>

  <div class="step-num" style="left:292px;top:146px">3</div>
  <p class="step-title" style="left:315px;top:151px">Automatisert postering</p>
  <p class="note" style="left:315px;top:163px">for hver konto</p>
  <svg class="icon" style="left:357px;top:178px" width="32" height="36"><use href="#ico-stack"/></svg>
  <svg class="icon" style="left:398px;top:192px" width="15" height="13"><use href="#ico-chevrons"/></svg>
  <svg class="icon" style="left:423px;top:178px" width="30" height="36"><use href="#ico-ledger"/></svg>

  <div class="step-num" style="left:537px;top:69px">4</div>
  <p class="step-title" style="left:561px;top:74px">Generere rapporter</p>
  <p class="note" style="left:561px;top:87px">Resultat, Balanse og kontantstrøm</p>
  <svg class="icon" style="left:618px;top:116px" width="25" height="36"><use href="#ico-report-text"/></svg>
  <svg class="icon" style="left:655px;top:116px" width="28" height="36"><use href="#ico-report-sheet"/></svg>
  <svg class="icon" style="left:696px;top:116px" width="28" height="36"><use href="#ico-report-cash"/></svg>

  <div class="phase phase--1">Levere</div>
  <div class="phase phase--2">Behandle</div>
  <div class="phase phase--3">Ferdigstille</div>
  <svg class="flow-arrow" style="left:269px"><use href="#ico-flow"/></svg>
  <svg class="flow-arrow" style="left:511px"><use href="#ico-flow"/></svg>
</section>

</body>
</html>
```